Upscale business cards needed for family business

We need professional business cards created for several family members. We are a family business holding company. We would like these relatively simple and straightforward, but also with a unique element to set them apart. Probably stick with neutral and simple colors - white, grey etc. We need space for the traditional elements, including name, title, address, email/phone number. And we will be creating several from this template so it needs to be template that is easy to switch information in and out of.

Industry/Entity Type

Business

Contact Information for Business Card

Please include the attached Dunmore Ventures logo.

Requirements
Must have
• The attached Dunmore Ventures logo.

```html
<!DOCTYPE html>
<html lang="en">
<head>
<meta charset="utf-8">
<title>Dunmore Ventures – Business Card</title>
<link rel="stylesheet" href="https://fonts.googleapis.com/css2?family=Cinzel:wght@400&family=Arimo:wght@400;700&display=swap">
<style>
  :root {
    --backdrop: #2b2b2d;
    --paper: #ffffff;
    --ink: #4a4a4a;
    --night: #141414;
    --night-soft: #262626;
    --gold: #d9a92a;
    --gold-light: #f2d46a;
    --gold-deep: #b98a1c;
    --white: #ffffff;
  }
  * { margin: 0; padding: 0; box-sizing: border-box; }
  html, body {
    width: 1200px; height: 843px; overflow: hidden;
    background: var(--backdrop);
  }
  .stage {
    position: relative; width: 1200px; height: 843px;
    display: flex; align-items: center; justify-content: center; gap: 40px;
  }
  .card {
    position: relative; width: 540px; height: 309px; overflow: hidden;
    box-shadow: 0 10px 28px rgba(0,0,0,.45);
  }

  /* Front */
  .card-front { background: var(--paper); }
  .front-brand {
    position: absolute; top: 0; left: 0; right: 0; height: 150px;
    display: flex; flex-direction: column; align-items: center; justify-content: center;
  }
  .brand-name {
    font-family: "Cinzel", serif; font-weight: 400;
    font-size: 28px; letter-spacing: 1px; color: var(--ink);
  }
  .brand-rule { width: 250px; height: 1px; background: var(--gold); margin: 6px 0 4px; }
  .brand-suffix {
    font-family: "Cinzel", serif; font-size: 10px; letter-spacing: 2px; color: var(--ink);
  }
  .front-panel { position: absolute; left: 0; top: 130px; width: 540px; height: 179px; }
  .front-panel svg { position: absolute; inset: 0; }
  .contact {
    position: absolute; left: 70px; top: 170px;
    font-family: "Arimo", sans-serif; color: var(--white);
  }
  .contact-name { font-size: 17px; letter-spacing: 1px; color: var(--gold); }
  .contact-title { font-size: 13px; letter-spacing: 1px; margin-top: 3px; }
  .contact-lines { margin-top: 12px; font-size: 12px; line-height: 17px; }

  /* Back */
  .card-back {
    background: linear-gradient(100deg, var(--gold-deep) 0%, var(--gold) 35%, var(--gold-light) 55%, var(--gold) 75%, var(--gold-deep) 100%);
    display: flex; flex-direction: column; align-items: center; justify-content: center;
  }
  .back-name {
    font-family: "Cinzel", serif; font-size: 32px; letter-spacing: 1px; color: var(--white);
  }
  .back-rule { width: 300px; height: 1px; background: var(--white); opacity: .85; margin: 8px 0 40px; }
  .back-web {
    font-family: "Arimo", sans-serif; font-size: 12px; letter-spacing: 4px; color: var(--white);
  }
</style>
</head>
<body>
<main class="stage">
  <section class="card card-front">
    <div class="front-brand">
      <div class="brand-name">Dunmore Ventures</div>
      <div class="brand-rule"></div>
      <div class="brand-suffix">INC</div>
    </div>
    <div class="front-panel">
      <svg width="540" height="179" viewBox="0 0 540 179" aria-hidden="true">
        <defs>
          <linearGradient id="panelShade" x1="0" y1="0" x2="1" y2="1">
            <stop offset="0" stop-color="var(--night-soft)"/>
            <stop offset="1" stop-color="var(--night)"/>
          </linearGradient>
        </defs>
        <path d="M0 30 Q270 -8 540 30 L540 179 L0 179 Z" fill="url(#panelShade)"/>
        <path d="M0 30 Q270 -8 540 30" fill="none" stroke="var(--gold)" stroke-width="4"/>
      </svg>
    </div>
    <div class="contact">
      <div class="contact-name">ELLIS MARLOW</div>
      <div class="contact-title">PRESIDENT</div>
      <div class="contact-lines">
        <div>2190 Ashford Lane</div>
        <div>Cedar Grove, NY 11020</div>
        <div>P : 555 210 4836</div>
        <div>E : ellis@dunmoreco.com</div>
        <div>W : www.dunmoreco.com</div>
      </div>
    </div>
  </section>

  <section class="card card-back">
    <div class="back-name">Dunmore Ventures</div>
    <div class="back-rule"></div>
    <div class="back-web">www.dunmoreco.com</div>
  </section>
</main>
</body>
</html>
```